Need DL Flyer for Real Estate Drops

We need a real estate flyer ,double sided. With content on 1 side like: Want to know what's your house is worth " contact us today and on other side agent details. We are looking for an ongoing partnership with designer so this assignment will be ongoing

```html
<!DOCTYPE html>
<html lang="en">
<head>
<meta charset="utf-8">
<title>Meridian Real Estate – DL Flyer</title>
<link href="https://fonts.googleapis.com/css2?family=Poppins:wght@400;500;600;700&display=swap" rel="stylesheet">
<style>
  :root{
    --navy:#101a4f;
    --red:#d3222a;
    --plum:#3b1e62;
    --wine:#8b1d3b;
    --white:#ffffff;
    --stage:#3a3a3c;
  }
  *{box-sizing:border-box;margin:0;padding:0}
  html,body{width:1200px;height:620px;overflow:hidden;background:var(--stage)}
  body{font-family:"Poppins",sans-serif;color:var(--white)}
  .canvas{position:relative;width:1200px;height:620px;overflow:hidden;background:var(--stage)}
  .flyer{position:absolute;top:20px;width:420px;height:580px;overflow:hidden;background:var(--navy);box-shadow:0 6px 18px rgba(0,0,0,.35)}
  .flyer--front{left:160px}
  .flyer--back{left:620px}
  .flyer__art{position:absolute;inset:0;width:420px;height:580px;display:block}

  .brand{position:absolute;display:flex;align-items:center;gap:7px;font-weight:600;font-size:15px;color:var(--white);white-space:nowrap}
  .brand__mark{width:13px;height:13px;background:var(--red)}
  .flyer--front .brand{top:34px;left:22px}
  .flyer--back .brand{top:250px;right:20px}

  .headline{position:absolute;top:108px;left:22px;width:180px;font-size:22px;line-height:27px;font-weight:700}
  .headline__cta{display:block;margin-top:10px;font-size:12.5px;line-height:15px;font-weight:600;width:90px}

  .about{position:absolute;top:360px;left:22px;width:205px}
  .about__title{font-size:19px;font-weight:600;margin-bottom:8px}
  .about__text{font-size:7px;line-height:13px;font-weight:400}

  .contact{position:absolute;top:462px;right:16px;text-align:right;color:var(--navy)}
  .contact__title{font-size:9.5px;font-weight:700;margin-bottom:8px}
  .contact__row{display:flex;justify-content:flex-end;align-items:center;gap:6px;margin-bottom:8px;font-size:9px;font-weight:600;color:var(--red)}
  .contact__row span{margin-left:4px}

  .icon{width:15px;height:15px;flex:none;display:block}

  .agent{position:absolute;top:286px;left:18px;width:230px}
  .agent__title{font-size:18px;font-weight:600;margin-bottom:6px}
  .agent__name{font-size:11.5px;font-weight:700;line-height:14px}
  .agent__role{font-size:7px;font-weight:600;margin-bottom:10px}
  .agent__row{display:flex;align-items:center;gap:8px;font-size:7.5px;margin-bottom:8px}
  .agent__row .icon{width:13px;height:13px}

  .follow{position:absolute;top:458px;right:20px;text-align:center;color:var(--navy)}
  .follow__title{font-size:8.5px;font-weight:600;margin-bottom:6px}
  .follow__list{display:flex;gap:8px}
  .follow__dot{width:9px;height:9px;border-radius:50%;background:var(--red)}
</style>
</head>
<body>
<main class="canvas">

  <section class="flyer flyer--front" aria-label="Flyer front">
    <svg class="flyer__art" viewBox="0 0 420 580">
      <defs>
        <linearGradient id="front-hero" x1="0" y1="0" x2="0.6" y2="1">
          <stop offset="0" stop-color="#3b1e62"/>
          <stop offset="1" stop-color="#8b1d3b"/>
        </linearGradient>
        <linearGradient id="front-photo-main" x1="0" y1="0" x2="0" y2="1">
          <stop offset="0" stop-color="#7fa8d8"/>
          <stop offset=".3" stop-color="#a9c4e2"/>
          <stop offset=".45" stop-color="#4f5f78"/>
          <stop offset=".62" stop-color="#c98b3e"/>
          <stop offset=".75" stop-color="#6b6f77"/>
          <stop offset="1" stop-color="#b8b4ab"/>
        </linearGradient>
        <linearGradient id="front-photo-a" x1="0" y1="0" x2="0" y2="1">
          <stop offset="0" stop-color="#9fb8d6"/>
          <stop offset=".45" stop-color="#dfe6ee"/>
          <stop offset=".65" stop-color="#4c5561"/>
          <stop offset="1" stop-color="#5d8a3a"/>
        </linearGradient>
        <linearGradient id="front-photo-b" x1="0" y1="0" x2="0" y2="1">
          <stop offset="0" stop-color="#8eb0d8"/>
          <stop offset=".45" stop-color="#c9d7e6"/>
          <stop offset=".65" stop-color="#8a6a50"/>
          <stop offset="1" stop-color="#a39784"/>
        </linearGradient>
        <linearGradient id="front-photo-c" x1="0" y1="0" x2="1" y2="1">
          <stop offset="0" stop-color="#f4f4f2"/>
          <stop offset=".5" stop-color="#4a5a6e"/>
          <stop offset="1" stop-color="#8b7a68"/>
        </linearGradient>
      </defs>
      <rect width="420" height="580" fill="var(--navy)"/>
      <path d="M0 0H420V230C380 262 330 300 250 322C160 342 80 342 0 346Z" fill="url(#front-hero)"/>
      <path d="M0 560C110 555 170 520 220 478C270 436 350 412 420 408V580H0Z" fill="var(--white)"/>
      <circle cx="330" cy="120" r="140" fill="url(#front-photo-main)" stroke="var(--white)" stroke-width="6" role="img" aria-label="Photo of a two-storey modern home at dusk"/>
      <circle cx="225" cy="288" r="48" fill="url(#front-photo-a)" stroke="var(--white)" stroke-width="5" role="img" aria-label="Photo of a single-storey grey home"/>
      <circle cx="312" cy="292" r="48" fill="url(#front-photo-b)" stroke="var(--white)" stroke-width="5" role="img" aria-label="Photo of a new brick home frontage"/>
      <circle cx="270" cy="370" r="55" fill="url(#front-photo-c)" stroke="var(--white)" stroke-width="5" role="img" aria-label="Photo of a bright open-plan living room"/>
    </svg>

    <div class="brand"><span class="brand__mark"></span>Meridian Real Estate</div>

    <h1 class="headline">Want to know what your house is worth
      <span class="headline__cta">Contact Us Today</span>
    </h1>

    <div class="about">
      <h2 class="about__title">About Us</h2>
      <p class="about__text">Meridian Real Estate is established in 2017 and has a dynamic team of sales and rentals. We are committed to the continuous professional development of all our team and employ the latest technology tools to provide an accurate, timely experience for our clients.</p>
    </div>

    <div class="contact">
      <p class="contact__title">Contact Us Today</p>
      <p class="contact__row">03 9100 4420
        <svg class="icon" viewBox="0 0 16 16"><circle cx="8" cy="8" r="8" fill="var(--navy)"/><path d="M5.5 4.2l1.4-.2.8 2-1 .8a5 5 0 0 0 2.5 2.5l.8-1 2 .8-.2 1.4c-3.5.5-6.8-2.8-6.3-6.3z" fill="var(--white)"/></svg>
        <span>0411 203 587</span>
        <svg class="icon" viewBox="0 0 16 16"><circle cx="8" cy="8" r="8" fill="var(--navy)"/><rect x="5.5" y="3.5" width="5" height="9" rx="1" fill="var(--white)"/></svg>
      </p>
      <p class="contact__row">rohan@meridianrealestate.com.au
        <svg class="icon" viewBox="0 0 16 16"><circle cx="8" cy="8" r="8" fill="var(--navy)"/><rect x="4" y="5" width="8" height="6" fill="var(--white)"/><path d="M4 5l4 3.2L12 5" fill="none" stroke="var(--navy)" stroke-width=".9"/></svg>
      </p>
    </div>
  </section>

  <section class="flyer flyer--back" aria-label="Flyer back">
    <svg class="flyer__art" viewBox="0 0 420 580">
      <defs>
        <linearGradient id="back-photo" x1="0" y1="0" x2="0" y2="1">
          <stop offset="0" stop-color="#e58a5c"/>
          <stop offset=".15" stop-color="#c98aa0"/>
          <stop offset=".28" stop-color="#7f9cc8"/>
          <stop offset=".42" stop-color="#d8d6d2"/>
          <stop offset=".6" stop-color="#8e9296"/>
          <stop offset=".78" stop-color="#5f9a45"/>
          <stop offset="1" stop-color="#a8a8a6"/>
        </linearGradient>
        <linearGradient id="back-portrait" x1="0" y1="0" x2="0" y2="1">
          <stop offset="0" stop-color="#f0f0f0"/>
          <stop offset=".5" stop-color="#9a9a9a"/>
          <stop offset="1" stop-color="#5a5a5a"/>
        </linearGradient>
      </defs>
      <rect width="420" height="580" fill="var(--navy)"/>
      <circle cx="200" cy="-40" r="280" fill="url(#back-photo)" stroke="var(--white)" stroke-width="8" role="img" aria-label="Photo of a modern double-storey home at sunset"/>
      <path d="M0 470C90 520 200 470 280 440C340 418 390 420 420 420V580H0Z" fill="var(--white)"/>
      <circle cx="330" cy="335" r="52" fill="url(#back-portrait)" stroke="var(--red)" stroke-width="5" role="img" aria-label="Portrait of the agent"/>
    </svg>

    <div class="brand"><span class="brand__mark"></span>Meridian Real Estate</div>

    <div class="agent">
      <h2 class="agent__title">Agent Contact</h2>
      <p class="agent__name">Rohan Mehra</p>
      <p class="agent__role">Managing Director/LEA, Meridian Real Estate</p>
      <p class="agent__row">
        <svg class="icon" viewBox="0 0 16 16"><circle cx="8" cy="8" r="8" fill="var(--white)"/><path d="M8 3.5a2.8 2.8 0 0 1 2.8 2.8C10.8 8.5 8 12 8 12S5.2 8.5 5.2 6.3A2.8 2.8 0 0 1 8 3.5z" fill="var(--navy)"/></svg>
        12/4 Horizon Drive, Westbrook 3030
      </p>
      <p class="agent__row">
        <svg class="icon" viewBox="0 0 16 16"><circle cx="8" cy="8" r="8" fill="var(--white)"/><path d="M5.5 4.2l1.4-.2.8 2-1 .8a5 5 0 0 0 2.5 2.5l.8-1 2 .8-.2 1.4c-3.5.5-6.8-2.8-6.3-6.3z" fill="var(--navy)"/></svg>
        03 9100 4420
        <svg class="icon" viewBox="0 0 16 16"><circle cx="8" cy="8" r="8" fill="var(--white)"/><rect x="5.5" y="3.5" width="5" height="9" rx="1" fill="var(--navy)"/></svg>
        0411 203 587
      </p>
      <p class="agent__row">
        <svg class="icon" viewBox="0 0 16 16"><circle cx="8" cy="8" r="8" fill="var(--white)"/><rect x="4" y="5" width="8" height="6" fill="var(--navy)"/><path d="M4 5l4 3.2L12 5" fill="none" stroke="var(--white)" stroke-width=".9"/></svg>
        rohan@meridianrealestate.com.au
      </p>
      <p class="agent__row">
        <svg class="icon" viewBox="0 0 16 16"><circle cx="8" cy="8" r="8" fill="var(--white)"/><circle cx="8" cy="8" r="4" fill="none" stroke="var(--navy)" stroke-width="1"/><path d="M4 8h8M8 4v8" stroke="var(--navy)" stroke-width="1"/></svg>
        www.meridianrealestate.com.au
      </p>
    </div>

    <div class="follow">
      <p class="follow__title">Follow Us</p>
      <div class="follow__list">
        <span class="follow__dot"></span><span class="follow__dot"></span><span class="follow__dot"></span><span class="follow__dot"></span><span class="follow__dot"></span>
      </div>
    </div>
  </section>

</main>
</body>
</html>
```